Loaf Harbor The Next Generation

we have a website www.loafharbor.ae which needs a complete graphical overhaul.
We are a bakery in Dubai, producing artisan breads and related products. Also salads and sandwiches. All fresh, all handmade, best quality.
We'd like to have something that looks fresh, modern, nice colours (no dark colours). Trendy but still transporting the feeling of the "good ol' bakery).
Our customers are expats, mostly english speakers. But we'd like to attract more different nationalities!
Also, customers are individuals and also companies (offices, airlines, yacht charters...) The third section are coffee shops, restaurants, hotels....
We have also an online shop. This is a MUST and can be optimised.
We'd like to stick with wordpress and woocommerce.
It MUST be responsive and easy to navigate on mobile devices. 60% of our customers order on mobile phones... browsing is even more.

Industry/Entity Type

Bakery

```html
<!DOCTYPE html>
<html lang="en">
<head>
<meta charset="utf-8">
<title>Loaf Harbor – Artisan Bakery</title>
<link href="https://fonts.googleapis.com/css2?family=Montserrat:wght@400;600;700;800&family=Open+Sans:wght@400;600&family=Playfair+Display:ital,wght@1,400&display=swap" rel="stylesheet">
<style>
:root{
  --green:#6b9a1e;
  --green-dark:#5e8a19;
  --ink:#2b2b2b;
  --brown:#5a4330;
  --muted:#8a8a8a;
  --line:#d9d9d9;
  --cream:#f8f1e4;
  --tan:#c79a5b;
  --red:#e0392b;
  --white:#ffffff;
}
*{margin:0;padding:0;box-sizing:border-box}
html,body{width:1200px;height:4144px;overflow:hidden}
body{font-family:"Open Sans",Arial,sans-serif;color:var(--ink);background:var(--white);position:relative}
.abs{position:absolute}
h2.section-title{font-family:"Montserrat",Arial,sans-serif;font-weight:700;font-size:30px;letter-spacing:2px;text-align:center;text-transform:uppercase;color:var(--ink)}
.section-sub{font-size:14px;color:var(--muted);text-align:center;line-height:1.6}

/* hero */
.hero{left:0;top:0;width:1200px;height:740px;background:
  radial-gradient(ellipse at 30% 55%,rgba(240,190,120,.8),transparent 55%),
  radial-gradient(ellipse at 75% 40%,rgba(214,120,80,.6),transparent 50%),
  linear-gradient(180deg,#d9a56c 0%,#e8bf8a 45%,#c98f5a 100%)}
.hero-shade{left:0;top:0;width:1200px;height:740px;background:rgba(90,50,20,.22)}
.topbar{left:0;top:0;width:1200px;height:32px;background:var(--green);color:var(--white);font-size:12px;display:flex;align-items:center;justify-content:space-between;padding:0 40px}
.topbar .right{display:flex;gap:14px;align-items:center}
.social-dot{width:12px;height:12px;border-radius:2px;background:rgba(255,255,255,.85);display:inline-block}
.brand{left:0;top:120px;width:1200px;display:flex;justify-content:center;align-items:center;gap:14px}
.brand-square{width:26px;height:26px;background:var(--white)}
.brand-name{font-family:"Montserrat",Arial,sans-serif;font-weight:800;font-size:46px;color:var(--white);letter-spacing:1px}
.main-nav{left:0;top:272px;width:1200px;display:flex;justify-content:center;gap:40px;font-family:"Montserrat",Arial,sans-serif;font-size:14px;font-weight:600;color:var(--white);text-transform:uppercase;letter-spacing:1px}
.hero-title{left:0;top:390px;width:1200px;text-align:center;font-family:"Montserrat",Arial,sans-serif;font-weight:700;font-size:100px;line-height:110px;letter-spacing:6px;color:var(--white)}
.hero-sub{left:0;top:508px;width:1200px;text-align:center;font-size:16px;color:var(--white)}
.btn-light{left:528px;top:564px;width:144px;height:46px;background:var(--white);color:var(--ink);font-family:"Montserrat",Arial,sans-serif;font-weight:700;font-size:13px;letter-spacing:1px;display:flex;align-items:center;justify-content:center}

/* features */
.features{left:0;top:740px;width:1200px;height:172px;background:var(--green);display:flex;padding:0 60px;align-items:center;gap:40px}
.feature{flex:1;display:flex;gap:16px;align-items:flex-start;color:var(--white)}
.feature svg{flex:none;margin-top:2px}
.feature h3{font-family:"Montserrat",Arial,sans-serif;font-size:20px;font-weight:700;text-transform:uppercase;margin-bottom:6px}
.feature p{font-size:13px;line-height:1.5;color:#eef5e2}

/* about */
.about-title{left:0;top:996px;width:1200px}
.about-text{left:260px;top:1048px;width:680px}
.about-left{left:60px;top:1140px;width:524px;height:380px;background:linear-gradient(135deg,#e6e2da,#a89d90 55%,#6e655c)}
.about-right{left:616px;top:1140px;width:524px;height:380px;background:radial-gradient(ellipse at 45% 55%,#e8b062,#c8823a 55%,#9a7258)}

/* products */
.products-title{left:0;top:1596px;width:1200px}
.products-sub{left:0;top:1646px;width:1200px}
.product{width:252px;height:320px;border:6px solid #ececec;outline:1px solid var(--line)}
.tag-best{left:8px;top:8px;background:var(--red);color:var(--white);font-family:"Montserrat",Arial,sans-serif;font-size:11px;font-weight:700;padding:4px 8px}
.product-overlay{left:0;top:0;width:240px;height:308px;background:rgba(107,154,30,.85);color:var(--white);text-align:center}
.overlay-icons{left:0;top:120px;width:240px;display:flex;justify-content:center;gap:14px}
.overlay-icons span{width:40px;height:40px;border-radius:50%;background:var(--white);display:flex;align-items:center;justify-content:center}
.overlay-name{left:0;top:180px;width:240px;font-family:"Montserrat",Arial,sans-serif;font-weight:700;font-size:17px}
.overlay-cat{left:0;top:206px;width:240px;font-size:12px;color:#eef5e2}
.overlay-price{left:0;top:232px;width:240px;font-family:"Montserrat",Arial,sans-serif;font-weight:700;font-size:24px}
.dots{left:586px;top:2398px;display:flex;gap:8px}
.dots span{width:12px;height:12px;border-radius:50%;border:2px solid #999}
.dots span.on{background:#999}
.btn-outline{left:480px;top:2446px;width:240px;height:48px;border:2px solid var(--ink);font-family:"Montserrat",Arial,sans-serif;font-weight:700;font-size:13px;letter-spacing:1px;display:flex;align-items:center;justify-content:center}

/* natural */
.natural{left:0;top:2580px;width:1200px;height:390px;background:
  radial-gradient(ellipse at 20% 50%,#a8c46a,transparent 45%),
  radial-gradient(ellipse at 70% 40%,#d9775a,transparent 40%),
  linear-gradient(180deg,#8fae5a,#6d8c3e)}
.natural-shade{left:0;top:2580px;width:1200px;height:390px;background:rgba(40,50,20,.3)}
.natural-label{left:530px;top:2788px;width:140px;height:20px;background:var(--white);color:var(--ink);font-size:9px;font-weight:600;letter-spacing:1px;display:flex;align-items:center;justify-content:center}
.natural-title{left:0;top:2820px;width:1200px;text-align:center;font-family:"Montserrat",Arial,sans-serif;font-weight:700;font-size:30px;letter-spacing:3px;color:var(--white)}

/* testimonials */
.testi-title{left:0;top:3020px;width:1200px}
.testi-sub{left:300px;top:3068px;width:600px}
.testi-card{width:344px;height:400px;border:2px solid var(--line);top:3168px;text-align:center;padding:0 34px}
.avatar{width:100px;height:100px;border-radius:50%;margin:60px auto 34px;background:linear-gradient(135deg,#e8d9c8,#a58a70)}
.testi-card p{font-size:13px;color:var(--muted);line-height:1.7}
.testi-name{margin-top:40px;font-size:12px;color:var(--ink)}
.testi-name b{font-weight:600}

/* footer */
.footer{left:0;top:3652px;width:1200px;height:448px;background:radial-gradient(ellipse at 50% 30%,#fffaf1,var(--cream) 70%);border-top:1px solid #eadfcb}
.footer-brand{left:0;top:3680px;width:1200px;display:flex;flex-direction:column;align-items:center;gap:18px}
.footer-circle{width:150px;height:150px;border-radius:50%;background:var(--tan)}
.footer-name{font-family:"Montserrat",Arial,sans-serif;font-weight:800;font-size:34px;color:var(--brown)}
.keep{left:0;top:3920px;width:1200px;text-align:center;font-family:"Playfair Display",Georgia,serif;font-style:italic;font-size:24px;letter-spacing:4px;color:var(--brown)}
.subscribe{left:320px;top:4016px;width:480px;height:40px;background:var(--white);border:1px solid var(--line);font-size:13px;color:#888;display:flex;align-items:center;padding-left:16px}
.join{left:800px;top:4016px;width:80px;height:40px;background:var(--green);color:var(--white);font-family:"Montserrat",Arial,sans-serif;font-weight:700;font-size:13px;display:flex;align-items:center;justify-content:center}
.bottom-bar{left:0;top:4100px;width:1200px;height:44px;background:var(--green-dark);color:var(--white);font-size:12px;display:flex;align-items:center;justify-content:space-between;padding:0 20px}
.bottom-bar nav{display:flex;gap:30px}
</style>
</head>
<body>

<header>
  <div class="abs hero" role="img" aria-label="Close-up photo of a stacked deli sandwich with tomatoes and greens"></div>
  <div class="abs hero-shade"></div>
  <div class="abs topbar">
    <span>Call: 04 555 0190</span>
    <div class="right">
      <span>Loaf Harbor, near Palm Court Plaza, Street 7, Dubai</span>
      <span class="social-dot"></span><span class="social-dot"></span><span class="social-dot"></span>
    </div>
  </div>
  <div class="abs brand"><span class="brand-square"></span><span class="brand-name">Loaf Harbor</span></div>
  <nav class="abs main-nav">
    <span>Welcome</span><span>Our Menu</span><span>Our Bakes</span><span>Chef British Pie</span><span>Order and Delivery</span><span>Get in Touch</span>
  </nav>
  <h1 class="abs hero-title">WELCOME</h1>
  <p class="abs hero-sub">Loaf Harbor Artisan Bakery, Where Everything is Handmade!</p>
  <div class="abs btn-light">BOOK A TABLE</div>
</header>

<section class="abs features">
  <div class="feature">
    <svg width="40" height="40" viewBox="0 0 40 40" fill="none" stroke="#fff" stroke-width="2"><path d="M8 32C8 16 20 8 34 8c0 14-8 26-24 24z"/><path d="M8 32L24 16"/></svg>
    <div><h3>Fresh Food</h3><p>Breads and salads prepared each morning with fresh, local ingredients.</p></div>
  </div>
  <div class="feature">
    <svg width="40" height="40" viewBox="0 0 40 40" fill="none" stroke="#fff" stroke-width="2"><path d="M11 24c-5 0-7-9 0-10 1-6 17-6 18 0 7 1 5 10 0 10z"/><rect x="12" y="24" width="16" height="8"/></svg>
    <div><h3>Chef's Specials</h3><p>Seasonal creations from our chefs, baked by hand in small batches.</p></div>
  </div>
  <div class="feature">
    <svg width="40" height="40" viewBox="0 0 40 40" fill="none" stroke="#fff" stroke-width="2"><path d="M8 16h20v8a8 8 0 0 1-8 8h-4a8 8 0 0 1-8-8z"/><path d="M28 18h3a3 3 0 0 1 0 6h-3"/><path d="M14 6v6M20 6v6"/></svg>
    <div><h3>Best Coffee</h3><p>Freshly roasted beans brewed to pair with every pastry we bake.</p></div>
  </div>
</section>

<section>
  <h2 class="abs section-title about-title">Loaf Harbor Bakery</h2>
  <p class="abs section-sub about-text">Are you searching for good bread? Our bakers shape every loaf by hand using slow fermentation, stone-milled flour and time-honoured methods, so each bite carries the warmth of a proper neighbourhood bakery.</p>
  <div class="abs about-left" role="img" aria-label="Photo of a baker serving at the counter of a bright café"></div>
  <div class="abs about-right" role="img" aria-label="Photo of a tray of golden croissants"></div>
</section>

<section>
  <h2 class="abs section-title products-title">Our Latest Bakery Products</h2>
  <p class="abs section-sub products-sub">Take a look at our newest bakes, made with passion every day</p>

  <div class="abs product" style="left:60px;top:1708px;background:linear-gradient(135deg,#e9e1d6,#8b6a4e)" role="img" aria-label="Photo of cappuccino cups on a table"></div>
  <div class="abs product" style="left:336px;top:1708px;background:linear-gradient(135deg,#c9873e,#6f8a2c 60%,#a5462d)" role="img" aria-label="Photo of a toasted club sandwich">
    <span class="abs tag-best">BEST</span>
  </div>
  <div class="abs product" style="left:612px;top:1708px;background:linear-gradient(135deg,#d8c6a4,#8a6a44)" role="img" aria-label="Photo of a walnut sourdough loaf">
    <div class="abs product-overlay">
      <div class="abs overlay-icons">
        <span><svg width="18" height="18" viewBox="0 0 20 20" fill="none" stroke="#6b9a1e" stroke-width="2"><circle cx="8" cy="8" r="6"/><path d="M13 13l5 5"/></svg></span>
        <span><svg width="18" height="18" viewBox="0 0 20 20" fill="none" stroke="#6b9a1e" stroke-width="2"><path d="M2 3h3l2 10h10l2-7H6"/><circle cx="8" cy="17" r="1.5"/><circle cx="15" cy="17" r="1.5"/></svg></span>
      </div>
      <div class="abs overlay-name">Walnut Sourdough</div>
      <div class="abs overlay-cat">Breads</div>
      <div class="abs overlay-price">$3.99</div>
    </div>
  </div>
  <div class="abs product" style="left:888px;top:1708px;background:linear-gradient(135deg,#c9d4b8,#7a5238 55%,#5a3a26)" role="img" aria-label="Photo of chocolate chip cookies"></div>

  <div class="abs product" style="left:60px;top:2052px;background:linear-gradient(135deg,#e7e3d8,#6f9a3a 55%,#b04a30)" role="img" aria-label="Photo of a fresh mixed salad bowl"></div>
  <div class="abs product" style="left:336px;top:2052px;background:linear-gradient(135deg,#ede6dc,#c99558 60%,#8b5a30)" role="img" aria-label="Photo of assorted pastries and croissants"></div>
  <div class="abs product" style="left:612px;top:2052px;background:linear-gradient(135deg,#d6b48a,#9a6b3e 55%,#7a3b3a)" role="img" aria-label="Photo of baguettes in paper bags">
    <span class="abs tag-best">BEST</span>
  </div>
  <div class="abs product" style="left:888px;top:2052px;background:linear-gradient(135deg,#7a5a44,#c7a07a 55%,#f0e6da)" role="img" aria-label="Photo of cakes and coffee on a wooden table"></div>

  <div class="abs dots"><span class="on"></span><span></span></div>
  <div class="abs btn-outline">SEE ALL OUR PRODUCTS</div>
</section>

<section>
  <div class="abs natural" role="img" aria-label="Photo of a colourful fresh salad"></div>
  <div class="abs natural-shade"></div>
  <div class="abs natural-label">A TASTE OF NATURE</div>
  <h2 class="abs natural-title">ONLY NATURAL INGREDIENTS</h2>
</section>

<section>
  <h2 class="abs section-title testi-title">Our Testimonials</h2>
  <p class="abs section-sub testi-sub">What our neighbours, offices and cafés say about our daily bakes, fresh from the oven every morning</p>

  <article class="abs testi-card" style="left:60px">
    <div class="avatar" role="img" aria-label="Portrait photo of a customer"></div>
    <p>The sourdough is the best in Dubai. Every order arrives fresh, warm and beautifully packed for our family weekend breakfasts.</p>
    <div class="testi-name"><b>Amelia Hart</b> – Food Lover</div>
  </article>
  <article class="abs testi-card" style="left:428px">
    <div class="avatar" role="img" aria-label="Portrait photo of a customer"></div>
    <p>Our team orders sandwiches and salads every week. Delivery is always on time and the quality never slips at all.</p>
    <div class="testi-name"><b>Omar Khalil</b> – Office Manager</div>
  </article>
  <article class="abs testi-card" style="left:796px">
    <div class="avatar" role="img" aria-label="Portrait photo of a customer"></div>
    <p>Guests at our café love the croissants. Reliable wholesale service and friendly bakers who truly care about their craft.</p>
    <div class="testi-name"><b>Lena Marsh</b> – Café Owner</div>
  </article>
</section>

<footer>
  <div class="abs footer"></div>
  <div class="abs footer-brand"><span class="footer-circle"></span><span class="footer-name">Loaf Harbor</span></div>
  <div class="abs keep">KEEP IN TOUCH</div>
  <div class="abs subscribe">Subscribe Here</div>
  <div class="abs join">JOIN</div>
  <div class="abs bottom-bar">
    <nav><span>Welcome</span><span>Our Menu</span><span>Our Bakes</span><span>Chef British Pie</span><span>Order and Delivery</span><span>Get in Touch</span></nav>
    <nav><span>Payment terms</span><span>Terms and Conditions</span><span>Privacy</span></nav>
  </div>
</footer>

</body>
</html>
```